Lumora vale- referral cards for new customers

Hey,

I would like 1 set of business cards with the following details:

10% off any sales / coupon code
Our phone number: 4702938165
Menu :Lumoravale.example (for the menu)
A line left blank to hand write an activation code: either on top or just on one side

Include the Lumora Vale logo ( your choice of black or white logo)
This card is to drive orders for people to order a cannabis order with Lumora Vale. Please make the logo a large part of the card on both sides.

Target Market(s)

People who consume cannabis 21 and up

Industry/Entity Type

Business

Contact Information for Business Card

This business card will be given to customers so they can then give it to other customers and generate referalls. We need this card to be elegant, impressionable, professional, and something worth keeping and passing to friends.

Font styles to use
Decorative
Script

Colors
33a6d7
85acd3
3176b5
0455a3
0592cd
85cae6
cee9f5
eaf1f7
757575

Requirements
Must have
• Our website
• Phone Number
• The 10% off an order
• Spot for activation code
Nice to have
• Eye catching design
• Look classy
• Textured feel or textured look
Should not have
• Do not look super cannabis heady
• Do not look attractive to children

```html
<!DOCTYPE html>
<html lang="en">
<head>
<meta charset="utf-8">
<title>Lumora Vale – Referral Card</title>
<link rel="stylesheet" href="https://fonts.googleapis.com/css2?family=Oswald:wght@700&family=Kaushan+Script&family=Roboto:wght@400;700&display=swap">
<style>
  :root {
    --backdrop: #e2e2e0;
    --card-light: #f6f6f4;
    --olive: #555a26;
    --olive-soft: #7d8450;
    --olive-deep: #474b1f;
    --ink: #1a1a1a;
    --muted: #555555;
    --white: #ffffff;
  }
  * { box-sizing: border-box; margin: 0; padding: 0; }
  html, body {
    width: 1200px; height: 960px; overflow: hidden;
    background: var(--backdrop);
    font-family: "Roboto", sans-serif;
  }
  .card {
    position: absolute;
    width: 600px; height: 343px;
    overflow: hidden;
    box-shadow: 2px 3px 4px rgba(0,0,0,0.35);
  }
  .card-front { left: 314px; top: 113px; background: var(--card-light); }
  .card-back  { left: 311px; top: 472px; background: var(--olive); }

  .offer { position: absolute; left: 39px; top: 42px; display: flex; align-items: flex-start; }
  .offer-percent {
    font-family: "Oswald", sans-serif; font-weight: 700;
    font-size: 76px; line-height: 1; color: var(--olive); letter-spacing: -5px;
    transform: scaleX(0.88); transform-origin: left top; margin-right: -16px;
  }
  .offer-detail { margin-left: 4px; margin-top: 2px; }
  .offer-off {
    display: block; font-family: "Oswald", sans-serif; font-weight: 700;
    font-size: 50px; line-height: 0.9; color: var(--ink); letter-spacing: -1px;
  }
  .offer-scope {
    display: block; font-family: "Kaushan Script", cursive;
    font-size: 18px; line-height: 1; color: var(--ink); margin-top: -1px;
  }

  .coupon { position: absolute; left: 40px; top: 192px; width: 208px; font-size: 14px; color: var(--ink); }
  .coupon-row { display: flex; align-items: baseline; }
  .coupon-fill { flex: 1; border-bottom: 1px dotted var(--muted); margin-left: 4px; height: 12px; }
  .coupon-extra { border-bottom: 1px dotted var(--muted); height: 1px; margin-top: 24px; }

  .contact { position: absolute; left: 39px; top: 267px; font-size: 14.5px; line-height: 19px; color: var(--muted); }
  .contact-label { font-weight: 700; color: var(--olive); }

  .emblem-front { position: absolute; left: 244px; top: 12px; }
  .emblem-back { position: absolute; left: 179px; top: 40px; }

  .brand-name {
    position: absolute; left: 0; right: 0; top: 250px;
    text-align: center; font-family: "Roboto", sans-serif; font-weight: 400;
    font-size: 36px; letter-spacing: 1px; color: var(--white);
  }
</style>
</head>
<body>
  <section class="card card-front">
    <div class="offer">
      <span class="offer-percent">10%</span>
      <span class="offer-detail">
        <span class="offer-off">OFF</span>
        <span class="offer-scope">any sales</span>
      </span>
    </div>

    <div class="coupon">
      <div class="coupon-row">Coupon code:<span class="coupon-fill"></span></div>
      <div class="coupon-extra"></div>
    </div>

    <div class="contact">
      <div><span class="contact-label">PHONE</span> : 4702938165</div>
      <div><span class="contact-label">MENU</span> : LUMORAVALE.EXAMPLE</div>
    </div>

    <svg class="emblem-front" width="356" height="326" viewBox="0 0 356 326" role="img" aria-label="Brand illustration area">
      <defs>
        <radialGradient id="front-glow" cx="50%" cy="50%" r="50%">
          <stop offset="0" stop-color="var(--olive-soft)" stop-opacity="0.55"/>
          <stop offset="0.7" stop-color="var(--olive-soft)" stop-opacity="0.25"/>
          <stop offset="1" stop-color="var(--olive-soft)" stop-opacity="0"/>
        </radialGradient>
      </defs>
      <rect width="356" height="326" fill="url(#front-glow)"/>
    </svg>
  </section>

  <section class="card card-back">
    <svg class="emblem-back" width="242" height="210" viewBox="0 0 242 210" role="img" aria-label="Brand illustration area">
      <defs>
        <radialGradient id="back-glow" cx="50%" cy="50%" r="50%">
          <stop offset="0" stop-color="var(--olive-deep)" stop-opacity="0.9"/>
          <stop offset="0.7" stop-color="var(--olive-deep)" stop-opacity="0.4"/>
          <stop offset="1" stop-color="var(--olive-deep)" stop-opacity="0"/>
        </radialGradient>
      </defs>
      <rect width="242" height="210" fill="url(#back-glow)"/>
    </svg>
    <div class="brand-name">Lumora Vale</div>
  </section>
</body>
</html>
```